Quorvex - Automated robotic Inspection with AI need new business cards

We need a new design of our business cards. The company is focused on automated quality control at high speed with unmatched results. We have a logo but need a more forward leaning business card that shows that we are delivering cutting edge technology.

Contact Information for Business Card

Name
Position
Adress
Phone
Email
e.g.
Lena Holmqvist
Chief Financial Officer (CFO)

Quorvex Sweden AB
Bruksvägen 14, SE-175 43 JÄRFÄLLA, Sweden
Mobile: +46735 21 47 83 | Office: +46 8 61 94 27
www.quorvex-example.com

Font styles to use
Sans Serif

```html
<!DOCTYPE html>
<html lang="en">
<head>
<meta charset="utf-8">
<title>Quorvex Business Card</title>
<link href="https://fonts.googleapis.com/css2?family=Lato:wght@400;700;900&display=swap" rel="stylesheet">
<style>
  :root {
    --backdrop: #e4e5e7;
    --card-white: #ffffff;
    --brand-blue: #1f5a8f;
    --brand-blue-deep: #174a78;
    --back-blue: #1f5b8a;
    --back-mark: #18507c;
    --text-grey: #3f4347;
  }
  * { margin: 0; padding: 0; box-sizing: border-box; }
  html, body {
    width: 1200px; height: 795px; overflow: hidden;
    background: var(--backdrop);
    font-family: "Lato", Arial, sans-serif;
  }
  .stage { position: relative; width: 1200px; height: 795px; }
  .card {
    position: absolute; top: 242px; width: 500px; height: 310px;
    box-shadow: 0 6px 18px rgba(0,0,0,0.18);
  }
  .card-front { left: 70px; background: var(--card-white); }
  .card-back { left: 630px; background: var(--back-blue); }

  .front-wordmark {
    position: absolute; right: 34px; top: 38px;
    font-weight: 900; font-size: 46px; letter-spacing: 3px;
    color: var(--brand-blue);
  }
  .divider-long {
    position: absolute; left: 160px; right: 12px; top: 128px;
    height: 2px; background: var(--brand-blue);
  }
  .person { position: absolute; left: 38px; top: 152px; }
  .person-name {
    font-weight: 700; font-size: 21px; letter-spacing: 0.5px;
    color: var(--brand-blue); text-transform: uppercase;
  }
  .person-title { font-size: 15px; color: var(--text-grey); margin-top: 2px; }
  .divider-short {
    position: absolute; left: 38px; top: 208px; width: 140px;
    height: 2px; background: var(--brand-blue);
  }
  .contacts { position: absolute; left: 38px; top: 220px; list-style: none; }
  .contacts li {
    display: flex; align-items: center; gap: 8px;
    font-size: 14px; line-height: 19px; color: var(--text-grey);
  }
  .contacts svg { width: 11px; height: 11px; flex: none; fill: var(--brand-blue); }
  .address {
    position: absolute; right: 30px; top: 150px; text-align: right;
    font-size: 13.5px; line-height: 18px; color: var(--text-grey);
  }
  .address-company { color: var(--brand-blue); }

  .back-wordmark {
    position: absolute; left: 0; right: 0; top: 50%;
    transform: translateY(-50%); text-align: center;
    font-weight: 900; font-size: 62px; letter-spacing: 4px;
    color: var(--back-mark);
  }
</style>
</head>
<body>
<main class="stage">
  <section class="card card-front" aria-label="Business card front">
    <div class="front-wordmark">Quorvex</div>
    <div class="divider-long"></div>

    <div class="person">
      <div class="person-name">Lena Holmqvist</div>
      <div class="person-title">Chief Financial Officer (CFO)</div>
    </div>
    <div class="divider-short"></div>

    <ul class="contacts">
      <li><svg viewBox="0 0 12 12" aria-hidden="true"><path d="M3 0h6a1 1 0 0 1 1 1v10a1 1 0 0 1-1 1H3a1 1 0 0 1-1-1V1a1 1 0 0 1 1-1zm0 1.5v8h6v-8zM6 10.2a.6.6 0 1 0 0 1.2.6.6 0 0 0 0-1.2z"/></svg>+46735 21 47 83</li>
      <li><svg viewBox="0 0 12 12" aria-hidden="true"><path d="M2.5 0.8l2 2.2-1 1.3c.7 1.5 1.8 2.6 3.2 3.2l1.3-1 2.2 2-1.2 1.9C5 10.2 1.8 7 0.6 2z"/></svg>+46 8 61 94 27</li>
      <li><svg viewBox="0 0 12 12" aria-hidden="true"><path d="M0 2h12v8H0zm1.2 1.2v.3L6 6.6l4.8-3.1v-.3z"/></svg>info@quorvex-example.com</li>
      <li><svg viewBox="0 0 12 12" aria-hidden="true"><circle cx="6" cy="6" r="5.5"/><path d="M0.8 6h10.4M6 0.5c-2.5 3-2.5 8 0 11M6 0.5c2.5 3 2.5 8 0 11" stroke="#fff" stroke-width="0.8" fill="none"/></svg>www.quorvex-example.com</li>
    </ul>

    <address class="address">
      <div class="address-company">Quorvex Sweden AB</div>
      <div>Bruksvägen 14, SE-175 43</div>
      <div>JÄRFÄLLA, Sweden</div>
    </address>
  </section>

  <section class="card card-back" aria-label="Business card back">
    <div class="back-wordmark">Quorvex</div>
  </section>
</main>
</body>
</html>
```